Makers' Hollow - Landing page for small and large screen

Makers’ Hollow gives you the space you need to take your side project from idea to reality.

With three days of focused work, it’s a place for you iron out the details of your business idea away from the distractions of the city.

The full copy and structure is here:
https://www.makershollow.example.co.uk/landing

What it needs, a touch of colour.

Target Market(s)

25-35 working in digital industry, software developer, a UI or UX designer

Number of Pages Required

1 page

Font styles to use
Sans Serif

Colors
0292cd
33b8a4
86cfc6
fdf9cf
ec1f27

Requirements
Should not have
• gradients or too much images

```html
<!DOCTYPE html>
<html lang="en">
<head>
<meta charset="utf-8">
<title>Makers' Hollow</title>
<link href="https://fonts.googleapis.com/css2?family=Montserrat:wght@400;500;600;700&family=Lato:wght@400;700&family=Poppins:wght@400&display=swap" rel="stylesheet">
<style>
:root{
  --blue:#1a7fc4;
  --blue-dark:#1f6fb5;
  --red:#e30613;
  --ink:#1f1f1f;
  --text:#2b2b2b;
  --grey-band:#ebebeb;
  --footer:#282828;
  --white:#ffffff;
}
*{box-sizing:border-box;margin:0;padding:0}
html,body{width:1200px;height:3125px;overflow:hidden;background:var(--white)}
body{position:relative;font-family:"Lato",sans-serif;color:var(--text)}
.abs{position:absolute}
.center{left:0;width:1200px;text-align:center}

/* header */
.site-header{top:0;left:0;width:1200px;height:140px;background:#fdf8f8}
.brand-name{left:100px;top:46px;font-family:"Montserrat",sans-serif;font-weight:600;font-size:32px;color:var(--blue)}
.contact-chip{top:24px;display:flex;gap:12px;align-items:flex-start}
.contact-chip .label{font-family:"Montserrat",sans-serif;font-weight:600;font-size:16px;color:var(--red)}
.contact-chip .value{font-family:"Montserrat",sans-serif;font-size:17px;color:var(--ink);margin-top:4px}
.contact-chip .value.small{font-size:15px}
.main-nav{top:96px;left:475px;display:flex;gap:30px;font-family:"Montserrat",sans-serif;font-size:17px;color:var(--ink)}
.nav-search{left:1090px;top:96px}

/* hero */
.hero{top:140px;left:0;width:1200px;height:582px;background:linear-gradient(160deg,#4a4a4a 0%,#303030 45%,#575757 100%)}
.hero-title{top:350px;font-family:"Montserrat",sans-serif;font-weight:600;font-size:58px;color:var(--white);letter-spacing:1px}
.hero-tagline{top:448px;font-family:"Montserrat",sans-serif;font-weight:500;font-size:42px;color:var(--white)}
.dot{display:inline-block;width:24px;height:24px;border-radius:50%;background:var(--white);margin:0 10px;vertical-align:middle}

/* intro */
.intro-heading{top:786px;font-family:"Montserrat",sans-serif;font-weight:600;font-size:29px;line-height:46px;color:var(--blue)}
.intro-copy{top:884px;left:142px;width:916px;text-align:center;font-size:16.2px;line-height:31px;color:var(--ink)}
.btn{background:var(--red);color:var(--white);font-family:"Montserrat",sans-serif;font-weight:700;font-size:17px;text-align:center;box-shadow:0 2px 4px rgba(0,0,0,.25)}
.btn-read{left:511px;top:1059px;width:178px;height:52px;line-height:52px}

/* features */
.features{top:1187px;left:0;width:1200px;height:452px;background:var(--blue)}
.features-heading{top:1259px;font-family:"Montserrat",sans-serif;font-weight:600;font-size:34px;color:var(--white)}
.feature{top:1355px;width:270px;text-align:center}
.feature-ring{width:136px;height:136px;border:3px solid var(--white);border-radius:50%;margin:0 auto;display:flex;align-items:center;justify-content:center}
.feature-caption{margin-top:26px;font-family:"Montserrat",sans-serif;font-weight:600;font-size:16.5px;line-height:29px;color:var(--white)}
.slider-arrow{top:1436px}

/* testimonials */
.testimonials-heading{top:1716px;font-family:"Montserrat",sans-serif;font-weight:600;font-size:32px;color:var(--blue-dark)}
.quote-mark{font-family:Georgia,serif;font-size:40px;color:var(--blue);font-style:italic}
.quote-text{top:1788px;left:150px;width:910px;text-align:center;font-size:15.8px;line-height:31px;color:var(--ink)}
.avatar{left:563px;top:1911px;width:94px;height:94px;border-radius:50%;background:linear-gradient(135deg,#c9a98a,#7d6552);border:3px solid #e6e6e6}
.author{left:672px;top:1933px}
.author-name{font-family:"Montserrat",sans-serif;font-weight:700;font-size:13px;color:var(--blue)}
.author-source{font-size:13px;font-style:italic;color:var(--ink);margin-top:6px}

/* contact */
.contact-band{top:2088px;left:0;width:1200px;height:882px;background:var(--grey-band)}
.contact-heading{top:2190px;left:0;width:1167px;text-align:center;font-family:"Montserrat",sans-serif;font-weight:600;font-size:33px;color:var(--blue)}
.contact-sub{top:2248px;left:0;width:1167px;text-align:center;font-family:"Montserrat",sans-serif;font-size:20px;color:var(--ink)}
.info-item{top:2306px;width:300px;text-align:center}
.info-icon{width:84px;height:84px;border-radius:50%;background:var(--red);margin:0 auto;display:flex;align-items:center;justify-content:center}
.info-text{margin-top:18px;font-family:"Montserrat",sans-serif;font-weight:500;font-size:17px;line-height:29px;color:#333}
.form-heading{top:2515px;font-family:"Montserrat",sans-serif;font-weight:600;font-size:33px;color:var(--blue)}
.field{background:var(--white);height:36px;border-radius:2px;font-family:"Poppins",sans-serif;font-size:12.5px;color:#555;padding:0 16px;display:flex;align-items:center;gap:6px}
.field.tall{height:146px;align-items:flex-start;padding-top:10px}
.btn-submit{left:512px;top:2808px;width:176px;height:52px;line-height:52px;font-size:18px;display:flex;align-items:center;justify-content:center;gap:10px}

/* footer */
.site-footer{top:2970px;left:0;width:1200px;height:155px;background:var(--footer)}
.social{top:3000px;left:529px;display:flex;gap:6px}
.social span{width:31px;height:31px;border:2px solid var(--white);border-radius:50%;display:block}
.footer-links{top:3054px;font-family:"Montserrat",sans-serif;font-size:17px;color:var(--white)}
.footer-links .sep{margin:0 8px}
.copyright{top:3092px;font-family:"Montserrat",sans-serif;font-size:15px;color:#dcdcdc}
</style>
</head>
<body>

<header class="abs site-header">
  <div class="abs brand-name">Makers' Hollow</div>

  <div class="abs contact-chip" style="left:472px">
    <svg width="44" height="44" viewBox="0 0 44 44" aria-hidden="true">
      <circle cx="22" cy="22" r="19" fill="none" stroke="#e30613" stroke-width="3"/>
      <path d="M15 13c2-1 3 0 4 3s0 3-1 4c1 3 3 5 6 6 1-1 2-2 4-1s4 2 3 4-3 3-6 2c-6-2-10-6-12-12-1-3 0-5 2-6z" fill="#e30613"/>
    </svg>
    <div><div class="label">Call us</div><div class="value">(555) 214 - 7730</div></div>
  </div>

  <div class="abs contact-chip" style="left:738px">
    <svg width="56" height="40" viewBox="0 0 56 40" aria-hidden="true">
      <rect x="2" y="4" width="52" height="32" fill="#e30613"/>
      <path d="M2 4l26 18L54 4M2 36l20-16M54 36L34 20" fill="none" stroke="#fff" stroke-width="2.5"/>
    </svg>
    <div><div class="label">Email us</div><div class="value small">support@makershollow.example.co.uk</div></div>
  </div>

  <nav class="abs main-nav">
    <span>HOME</span><span>ABOUT US</span><span>JOIN US</span><span>ORGANISERS</span><span>CONTACT US</span>
  </nav>
  <svg class="abs nav-search" width="20" height="20" viewBox="0 0 20 20" aria-hidden="true">
    <circle cx="8" cy="8" r="6" fill="none" stroke="#1f1f1f" stroke-width="3"/>
    <path d="M12.5 12.5l5.5 5.5" stroke="#1f1f1f" stroke-width="3.5" stroke-linecap="round"/>
  </svg>
</header>

<section class="abs hero" role="img" aria-label="Overhead photo of a creative's desk with keyboard, lamp, camera and coffee"></section>
<h1 class="abs center hero-title">MAKERS' HOLLOW</h1>
<p class="abs center hero-tagline">create<span class="dot"></span>connect<span class="dot"></span>collaborate</p>

<h2 class="abs center intro-heading">Makers’ Hollow gives you the space you need to<br>take your side project from idea to reality.</h2>
<p class="abs intro-copy">Calling all creatives! Whether you’re a software developer, a UI or UX designer, a product creator or an artworker, you’ll know only too well that great work rarely materialises when you’re in the wrong environment. Phones buzzing. Emails pinging. Chat calls incoming...distractions are everywhere – and they do nothing for your motivation. So, if you have a seed of a business idea and need to reclaim some focus, Makers’ Hollow is for you. Or maybe you’ve created a product, sought a patent and you’re ready – and raring – to go.</p>
<div class="abs btn btn-read">READ MORE</div>

<section class="abs features"></section>
<h2 class="abs center features-heading">JOIN THE RETREAT AND ENJOY</h2>

<svg class="abs slider-arrow" style="left:28px" width="20" height="36" viewBox="0 0 20 36" aria-hidden="true"><path d="M17 2L3 18l14 16" fill="none" stroke="#fff" stroke-width="2"/></svg>
<svg class="abs slider-arrow" style="left:1152px" width="20" height="36" viewBox="0 0 20 36" aria-hidden="true"><path d="M3 2l14 16L3 34" fill="none" stroke="#fff" stroke-width="2"/></svg>

<div class="abs feature" style="left:48px">
  <div class="feature-ring">
    <svg width="72" height="72" viewBox="0 0 72 72" fill="none" stroke="#fff" stroke-width="2.5" aria-hidden="true">
      <circle cx="36" cy="14" r="6"/><path d="M26 30c0-6 4-9 10-9s10 3 10 9z"/>
      <circle cx="16" cy="44" r="6"/><path d="M6 60c0-6 4-9 10-9s10 3 10 9z"/>
      <circle cx="56" cy="44" r="6"/><path d="M46 60c0-6 4-9 10-9s10 3 10 9z"/>
      <path d="M20 28a20 20 0 0 0-6 10M52 28a20 20 0 0 1 6 10M28 62h16"/>
    </svg>
  </div>
  <p class="feature-caption">Three, full days of<br>distraction-free work</p>
</div>

<div class="abs feature" style="left:302px">
  <div class="feature-ring">
    <svg width="72" height="72" viewBox="0 0 72 72" fill="none" stroke="#fff" stroke-width="2.5" aria-hidden="true">
      <rect x="24" y="10" width="26" height="52"/><rect x="12" y="34" width="12" height="28"/><rect x="50" y="28" width="12" height="34"/>
      <path d="M30 18h4M40 18h4M30 28h4M40 28h4M30 38h4M40 38h4M30 48h4M40 48h4M8 62h58"/>
    </svg>
  </div>
  <p class="feature-caption">A chance to hone your side<br>project away from the office</p>
</div>

<div class="abs feature" style="left:573px">
  <div class="feature-ring">
    <svg width="72" height="72" viewBox="0 0 72 72" fill="none" stroke="#fff" stroke-width="2.5" aria-hidden="true">
      <path d="M24 62V50c-6-4-9-10-9-17 0-12 9-20 21-20s20 8 20 18l5 9h-5v8c0 3-2 5-5 5h-6v9"/>
      <circle cx="32" cy="30" r="7"/><path d="M32 15v-6M20 20l-4-4M44 20l4-4M14 30H8"/>
    </svg>
  </div>
  <p class="feature-caption">The opportunity to collaborate<br>with like minded creatives</p>
</div>

<div class="abs feature" style="left:848px">
  <div class="feature-ring">
    <svg width="72" height="72" viewBox="0 0 72 72" fill="#fff" aria-hidden="true">
      <path d="M20 8l2.4 5 5.4.6-4 3.7 1 5.3-4.8-2.7-4.8 2.7 1-5.3-4-3.7 5.4-.6zM36 6l2.4 5 5.4.6-4 3.7 1 5.3L36 23l-4.8 2.6 1-5.3-4-3.7 5.4-.6zM52 8l2.4 5 5.4.6-4 3.7 1 5.3-4.8-2.7-4.8 2.7 1-5.3-4-3.7 5.4-.6z"/>
      <circle cx="36" cy="36" r="6"/><path d="M24 60c0-9 5-14 12-14s12 5 12 14z"/>
      <circle cx="16" cy="40" r="5"/><path d="M6 60c0-8 4-12 10-12 3 0 5 1 7 3-2 3-3 6-3 9z"/>
      <circle cx="56" cy="40" r="5"/><path d="M66 60c0-8-4-12-10-12-3 0-5 1-7 3 2 3 3 6 3 9z"/>
    </svg>
  </div>
  <p class="feature-caption">Good, honest feedback and<br>insight from fellow attendees</p>
</div>

<h2 class="abs center testimonials-heading">TESTIMONIALS</h2>
<span class="abs quote-mark" style="left:136px;top:1754px">“</span>
<p class="abs quote-text">At vero eos et accusamus et iusto odio dignissimos ducimus qui blanditiis praesentium voluptatum deleniti atque corrupti quos dolores et quas molestias excepturi sint occaecati cupiditate non provident, similique sunt in culpa qui officia deserunt mollitia animi, id est laborum et dolorum fuga. Et harum quidem rerum facilis est et expedita distinctio.</p>
<span class="abs quote-mark" style="left:1040px;top:1846px">”</span>
<div class="abs avatar" role="img" aria-label="Portrait photo of the reviewer"></div>
<div class="abs author">
  <div class="author-name">– DANA WHITLOW</div>
  <div class="author-source">via guest reviews</div>
</div>

<section class="abs contact-band"></section>
<h2 class="abs contact-heading">CONTACT INFORMATION</h2>
<p class="abs contact-sub">Contact us for more information</p>

<div class="abs info-item" style="left:100px">
  <div class="info-icon">
    <svg width="44" height="50" viewBox="0 0 44 50" fill="none" stroke="#fff" stroke-width="2.5" aria-hidden="true">
      <path d="M22 36C14 26 10 20 10 14a12 12 0 0 1 24 0c0 6-4 12-12 22z"/><circle cx="22" cy="14" r="5"/>
      <ellipse cx="22" cy="40" rx="16" ry="6"/>
    </svg>
  </div>
  <p class="info-text">214 Millbrook Lane<br>Oakridge, NC 27019</p>
</div>

<div class="abs info-item" style="left:450px">
  <div class="info-icon">
    <svg width="44" height="44" viewBox="0 0 44 44" fill="none" stroke="#fff" stroke-width="2.5" aria-hidden="true">
      <path d="M10 6c3-2 5 0 7 4s1 5-1 7c2 5 5 8 10 10 2-2 4-3 7-1s5 4 3 7-5 4-9 3C18 33 11 26 8 17 7 12 7 8 10 6z"/>
      <path d="M26 8a10 10 0 0 1 10 10M26 2a16 16 0 0 1 16 16"/>
    </svg>
  </div>
  <p class="info-text">Phone:<br>(555) 214 - 7730</p>
</div>

<div class="abs info-item" style="left:783px">
  <div class="info-icon">
    <svg width="46" height="34" viewBox="0 0 46 34" fill="none" stroke="#fff" stroke-width="2.5" aria-hidden="true">
      <rect x="2" y="2" width="42" height="30"/><path d="M2 2l21 17L44 2M2 32l16-14M44 32L28 18"/>
    </svg>
  </div>
  <p class="info-text">Email:<br>info@makershollow.example.co.uk</p>
</div>

<h2 class="abs center form-heading">CONTACT US</h2>

<div class="abs field" style="left:165px;top:2586px;width:425px">👤 First Name</div>
<div class="abs field" style="left:165px;top:2640px;width:425px">▮ Company</div>
<div class="abs field" style="left:165px;top:2694px;width:425px">✉ Email Address</div>
<div class="abs field" style="left:165px;top:2748px;width:425px">✆ Phone Number</div>
<div class="abs field" style="left:610px;top:2586px;width:427px">👤 Last Name</div>
<div class="abs field tall" style="left:610px;top:2640px;width:427px">✎ Message :</div>

<div class="abs btn btn-submit">
  <svg width="20" height="18" viewBox="0 0 20 18" aria-hidden="true"><path d="M19 1L1 8l6 2 1 7 3-5 5 3z" fill="#fff"/></svg>
  Submit
</div>

<footer class="abs site-footer"></footer>
<div class="abs social" aria-label="Social links">
  <span></span><span></span><span></span><span></span>
</div>
<p class="abs center footer-links">Home<span class="sep">|</span>About Us<span class="sep">|</span>Join Us<span class="sep">|</span>Organisers<span class="sep">|</span>Contact Us</p>
<p class="abs center copyright">© 2019 Company Name&nbsp; All right reserved</p>

</body>
</html>
```